Business Cards, Letterheads, Envelopes

A company's new identity to be reflected on its stationery items

Target Market(s)

Large Corporate Companies & Enterprises

Font styles to use
Sans Serif

Colors
0555a3
3176b5
85abd2
85cae6
33a6d7
0293ce

```html
<!DOCTYPE html>
<html lang="en">
<head>
<meta charset="utf-8">
<title>Corvane Systems – Stationery</title>
<link href="https://fonts.googleapis.com/css2?family=Source+Sans+3:wght@400;600&display=swap" rel="stylesheet">
<style>
  :root {
    --navy: #16203a;
    --royal: #0a44f5;
    --sky: #35b5f5;
    --brand: #3aa0e8;
    --grey: #7d8590;
    --white: #ffffff;
    --canvas: #ffffff;
  }
  * { box-sizing: border-box; margin: 0; padding: 0; }
  html, body { width: 1200px; height: 603px; overflow: hidden; background: var(--canvas); }
  body { position: relative; font-family: "Source Sans 3", sans-serif; }

  .sheet {
    position: absolute;
    background: var(--white);
    overflow: hidden;
    box-shadow: 6px 8px 10px rgba(0,0,0,0.45);
  }
  .sheet svg.shapes { position: absolute; left: 0; top: 0; width: 100%; height: 100%; }

  .brand {
    position: absolute;
    display: flex;
    align-items: center;
    gap: 10px;
  }
  .brand-dot { border-radius: 50%; background: var(--brand); flex: none; }
  .brand-name {
    color: var(--brand);
    font-weight: 600;
    text-transform: uppercase;
    letter-spacing: 0.06em;
    white-space: nowrap;
    line-height: 1;
  }

  /* business card front */
  .card-front { left: 8px; top: 36px; width: 317px; height: 182px; }
  .card-front .brand { left: 60px; top: 20px; }
  .card-front .brand-dot { width: 48px; height: 48px; }
  .card-front .brand-name { font-size: 19px; }

  /* business card back */
  .card-back { left: 350px; top: 34px; width: 318px; height: 182px; }
  .card-back .tab {
    position: absolute; left: 0; top: 44px; width: 10px; height: 96px;
    background: var(--royal); border-radius: 0 6px 6px 0;
  }
  .card-back .brand { left: 14px; top: 74px; gap: 7px; }
  .card-back .brand-dot { width: 32px; height: 32px; }
  .card-back .brand-name { font-size: 11px; }
  .card-back .contact-panel {
    position: absolute; right: 0; top: 0; width: 159px; height: 182px;
    background: var(--navy);
    border-bottom-left-radius: 58px;
    color: var(--white);
  }
  .person { position: absolute; right: 24px; top: 9px; text-align: right; color: #d4d8de; }
  .person-name { font-size: 11.5px; line-height: 1.2; }
  .person-role { font-size: 8px; }
  .contact-list { position: absolute; left: 16px; top: 57px; list-style: none; }
  .contact-list li {
    display: flex; align-items: center; gap: 7px;
    font-size: 8px; height: 14px; margin-bottom: 14px; color: #e7eaee;
  }
  .contact-list li:nth-child(3) { margin-bottom: 8px; }
  .contact-list svg { width: 12px; height: 12px; fill: var(--white); flex: none; }

  /* envelope */
  .envelope { left: 9px; top: 270px; width: 610px; height: 286px; border-radius: 6px; }
  .envelope .brand { left: 22px; top: 22px; }
  .envelope .brand-dot { width: 52px; height: 52px; }
  .envelope .brand-name { font-size: 17px; }

  /* letterhead */
  .letterhead { left: 713px; top: 8px; width: 422px; height: 575px; border-radius: 4px; }
  .letterhead .brand { left: 14px; top: 42px; gap: 8px; }
  .letterhead .brand-dot { width: 40px; height: 40px; }
  .letterhead .brand-name { font-size: 14px; }
  .letterhead .footer-line {
    position: absolute; right: 2px; top: 524px;
    font-size: 7px; color: var(--grey); white-space: nowrap;
  }
</style>
</head>
<body>

  <section class="sheet card-front" aria-label="Business card front">
    <svg class="shapes" viewBox="0 0 317 182" preserveAspectRatio="none" aria-hidden="true">
      <path fill="var(--royal)" d="M29,182 C40,162 60,153 88,153 L110,153 L110,182 Z"/>
      <path fill="var(--navy)" d="M71,182 C78,155 100,140 135,140 L317,140 L317,182 Z"/>
    </svg>
    <div class="brand">
      <span class="brand-dot"></span>
      <span class="brand-name">Corvane Systems</span>
    </div>
  </section>

  <section class="sheet card-back" aria-label="Business card back">
    <span class="tab"></span>
    <div class="brand">
      <span class="brand-dot"></span>
      <span class="brand-name">Corvane Systems</span>
    </div>
    <div class="contact-panel">
      <div class="person">
        <p class="person-name">Daniel Marsh</p>
        <p class="person-role">CEO</p>
      </div>
      <ul class="contact-list">
        <li>
          <svg viewBox="0 0 24 24" aria-hidden="true"><path d="M12 1a8 8 0 0 0-8 8c0 6 8 14 8 14s8-8 8-14a8 8 0 0 0-8-8zm0 11a3 3 0 1 1 0-6 3 3 0 0 1 0 6z"/></svg>
          No.14, Harbor Lane, DC
        </li>
        <li>
          <svg viewBox="0 0 24 24" aria-hidden="true"><path d="M6.6 10.8a15.5 15.5 0 0 0 6.6 6.6l2.2-2.2a1 1 0 0 1 1-.25 11.4 11.4 0 0 0 3.6.57 1 1 0 0 1 1 1V20a1 1 0 0 1-1 1A17 17 0 0 1 3 4a1 1 0 0 1 1-1h3.5a1 1 0 0 1 1 1c0 1.25.2 2.450.57 3.6a1 1 0 0 1-.25 1z"/></svg>
          0500-312-7740
        </li>
        <li>
          <svg viewBox="0 0 24 24" aria-hidden="true"><path d="M2 5h20v14H2z M3.5 6.5l8.5 6.5 8.5-6.5" stroke="var(--navy)" stroke-width="1.4"/></svg>
          info@corvanesys.com
        </li>
        <li>
          <svg viewBox="0 0 24 24" aria-hidden="true"><path d="M5 2l13 12h-6l4 8-3 1.5-4-8-4 4z"/></svg>
          www.corvanesys.com
        </li>
      </ul>
    </div>
  </section>

  <section class="sheet envelope" aria-label="Envelope">
    <svg class="shapes" viewBox="0 0 610 286" preserveAspectRatio="none" aria-hidden="true">
      <path fill="var(--royal)" d="M0,126 C90,240 220,268 350,266 L380,264 L380,286 L0,286 Z"/>
      <path fill="var(--sky)" d="M343,286 C350,268 366,258 390,258 L410,258 L410,286 Z"/>
      <path fill="var(--royal)" d="M382,286 C388,262 410,247 442,247 L610,247 L610,286 Z"/>
    </svg>
    <div class="brand">
      <span class="brand-dot"></span>
      <span class="brand-name">Corvane Systems</span>
    </div>
  </section>

  <section class="sheet letterhead" aria-label="Letterhead">
    <svg class="shapes" viewBox="0 0 422 575" preserveAspectRatio="none" aria-hidden="true">
      <path fill="var(--sky)" d="M164,34 L259,0 L422,0 L422,77 C362,22 250,14 164,34 Z"/>
      <path fill="var(--royal)" d="M0,460 C40,515 80,545 140,556 L140,575 L0,575 Z"/>
      <path fill="var(--sky)" d="M124,575 C132,555 152,544 182,544 L200,544 L200,575 Z"/>
      <path fill="var(--royal)" d="M166,575 C172,548 192,531 226,531 L422,531 L422,575 Z"/>
    </svg>
    <div class="brand">
      <span class="brand-dot"></span>
      <span class="brand-name">Corvane Systems</span>
    </div>
    <p class="footer-line">No.14, Harbor Lane, DC, 0500-312-7740, info@corvanesys.com, www.corvanesys.com</p>
  </section>

</body>
</html>
```